Billboard for Law Firm

I am looking for a billboard designs. Our branding right now is not good. The logo has to stay the same, but please help come up with something modern, airy, perhaps geometric for the supporting design elements.
Colors should probably be red and blue, or shades of blue, but you can play with the exact shades. Doesn't have to match what you see in the attachment.

The billboard should include:

- Some type of design to bring it to life.

- Logo

- Accident & Injury Law

- 614.300.7000

- Disclaimer (very small text): No Representation Made That The Quality of Legal Services Performed is Greater Than the Those of Other Attorneys

Slogan (very large): Grits, Gravy, and a Good Attorney

______________

Target Market(s)

Southern United States

Industry/Entity Type

Legal Services

Font styles to use
Serif
Sans Serif

Colors
0054AA
0677BA
7BADD7
CADEEF
E8F1F8
EB3D1F
EC4F4E
F09395
F8D3D4
FCEDEE

Requirements
Must have
• Help Make it Memorable and Easy to Read (large text for slogan)
Nice to have
• Some shapes or design elements that may become part of our branding.

```html
<!DOCTYPE html>
<html lang="en">
<head>
<meta charset="UTF-8">
<title>Hartwell Firm Billboard</title>
<link rel="stylesheet" href="https://fonts.googleapis.com/css2?family=Jost:wght@300;400;600;700;800&display=swap">
<style>
  :root {
    --brand-red: #e0101f;
    --brand-blue: #2b2f9a;
    --flame-red: #d9101c;
    --flame-blue: #2f3a9c;
    --paper: #ffffff;
    --stage: #e3e9f0;
  }
  * { margin: 0; padding: 0; box-sizing: border-box; }
  html, body {
    width: 1200px;
    height: 800px;
    overflow: hidden;
    background: var(--stage);
    font-family: "Jost", "Futura", sans-serif;
  }
  .billboard {
    position: absolute;
    left: 20px;
    top: 110px;
    width: 1160px;
    height: 580px;
    background: var(--paper);
    overflow: hidden;
  }
  .emblem-art {
    position: absolute;
    left: 0;
    top: 0;
    width: 300px;
    height: 580px;
    background:
      linear-gradient(135deg, var(--flame-blue) 0%, var(--flame-blue) 22%, transparent 22%),
      linear-gradient(180deg, #f3c7ca 0%, var(--flame-red) 55%, #b50d18 100%);
    clip-path: polygon(0 0, 78% 0, 100% 40%, 92% 75%, 80% 100%, 0 100%);
  }
  .logo {
    position: absolute;
    left: 500px;
    top: 40px;
    display: flex;
    align-items: center;
    gap: 10px;
    white-space: nowrap;
  }
  .logo-mark {
    width: 20px;
    height: 20px;
    border-radius: 50%;
    background: var(--brand-red);
    flex: none;
  }
  .logo-name {
    font-weight: 600;
    font-size: 24px;
    line-height: 1;
    letter-spacing: 1px;
    color: var(--brand-red);
    text-transform: uppercase;
  }
  .frame-lines {
    position: absolute;
    left: 0;
    top: 0;
    width: 1160px;
    height: 580px;
    pointer-events: none;
  }
  .slogan {
    position: absolute;
    left: 340px;
    top: 108px;
    line-height: 1;
    text-transform: uppercase;
  }
  .slogan-line {
    display: block;
    white-space: nowrap;
    font-size: 70px;
  }
  .slogan-line--first { padding-left: 80px; }
  .slogan-line--second { margin-top: 8px; }
  .slogan-strong {
    font-weight: 700;
    color: var(--brand-red);
  }
  .slogan-light {
    font-weight: 300;
    color: var(--brand-blue);
  }
  .practice-area {
    position: absolute;
    left: 420px;
    top: 282px;
    width: 400px;
    height: 50px;
    border: 3px solid var(--brand-blue);
    display: flex;
    align-items: center;
    justify-content: center;
    white-space: nowrap;
    font-weight: 600;
    font-size: 27px;
    letter-spacing: 1.5px;
    color: var(--brand-blue);
    text-transform: uppercase;
  }
  .phone-band {
    position: absolute;
    left: 380px;
    top: 370px;
    width: 740px;
    height: 100px;
    background: var(--brand-red);
    display: flex;
    align-items: center;
    padding-left: 72px;
  }
  .phone-number {
    font-weight: 700;
    font-size: 82px;
    line-height: 1;
    letter-spacing: 2px;
    white-space: nowrap;
    color: var(--paper);
  }
  .phone-badge {
    position: absolute;
    left: 330px;
    top: 368px;
    width: 104px;
    height: 104px;
    border-radius: 50%;
    background: var(--brand-blue);
    border: 6px solid var(--paper);
    display: flex;
    align-items: center;
    justify-content: center;
  }
  .phone-badge svg { width: 46px; height: 46px; }
</style>
</head>
<body>
  <main class="billboard">
    <div class="emblem-art" role="img" aria-label="Large red and blue flame emblem decoration"></div>

    <div class="logo">
      <span class="logo-mark"></span>
      <span class="logo-name">The Hartwell Firm</span>
    </div>

    <svg class="frame-lines" viewBox="0 0 1160 580" aria-hidden="true">
      <g fill="none" stroke="var(--brand-blue)" stroke-width="3">
        <path d="M400 170 V90 H945 V180"/>
        <path d="M385 270 V307 H420"/>
        <path d="M820 307 H945 V270"/>
      </g>
    </svg>

    <h1 class="slogan">
      <span class="slogan-line slogan-line--first">
        <span class="slogan-strong">Grits, Gravy</span>
      </span>
      <span class="slogan-line slogan-line--second">
        <span class="slogan-light">A</span>
        <span class="slogan-strong">Good</span>
        <span class="slogan-light">Attorney</span>
      </span>
    </h1>

    <p class="practice-area">Accident &amp; Injury Law</p>

    <div class="phone-band">
      <span class="phone-number">614.300.7000</span>
    </div>
    <div class="phone-badge">
      <svg viewBox="0 0 24 24" aria-hidden="true">
        <path fill="#ffffff" d="M6.6 10.8a15.1 15.1 0 0 0 6.6 6.6l2.2-2.2a1 1 0 0 1 1-.25 11.4 11.4 0 0 0 3.6.57 1 1 0 0 1 1 1V20a1 1 0 0 1-1 1A17 17 0 0 1 3 4a1 1 0 0 1 1-1h3.5a1 1 0 0 1 1 1c0 1.25.2 2.45.57 3.57a1 1 0 0 1-.25 1z"/>
      </svg>
    </div>
  </main>
</body>
</html>
```